Venture Northvale Loan Firm

We are looking to overhaul our existing website (substantially), with only using the same logos (which we can provide).
We are an investment firm that focuses on making loans to late stage technology companies. Our site should ultimately look like other venture capital firms, and look modern and fresh. We have an existing website www.northvaleloan.com which this will be replacing, although we will be using a lot of the existing written content, and potentially the numbers of pages we will need, we are not wed to anything else. Please feel free to shoot any questions at any time and thank you in advance for your help!
Websites we like as examples:
https://www.tkbrandel.com/
https://www.emberwoodfunds.com/
Target Market(s)
Potential investors who will invest in our firm, as well as potentially companies that are looking to borrow money from us.

```html
<!DOCTYPE html>
<html lang="en">
<head>
<meta charset="utf-8">
<title>Northvale Loan — Structured Credit Investment</title>
<link href="https://fonts.googleapis.com/css2?family=Roboto:wght@300;400;500;700&display=swap" rel="stylesheet">
<style>
:root{
  --green:#43b649;
  --yellow:#f6c21c;
  --pink:#e8266f;
  --ink:#2f3437;
  --text:#6d7378;
  --muted:#a3a8ad;
  --line:#e6e8ea;
  --paper:#ffffff;
  --soft:#f4f6f7;
  --band:#393c3e;
}
*{box-sizing:border-box;margin:0;padding:0}
html,body{width:1200px;height:2700px;overflow:hidden}
body{font-family:"Roboto",Arial,sans-serif;color:var(--text);background:var(--paper);position:relative}

/* top bar */
.topbar{height:30px;border-bottom:1px solid var(--line);display:flex;align-items:center;justify-content:space-between;padding:0 150px;font-size:11px;color:var(--muted)}
.topbar .socials{display:flex;gap:8px}
.topbar .socials span{width:10px;height:10px;border-radius:50%;background:#c9cdd1;display:block}
.topbar .call{display:flex;align-items:center;gap:6px}

/* nav */
.nav{height:48px;display:flex;align-items:center;justify-content:space-between;padding:0 150px;border-bottom:1px solid var(--line)}
.brand{display:flex;align-items:center;gap:8px;font-size:17px;font-weight:500;color:var(--ink);letter-spacing:.5px}
.brand i{width:18px;height:18px;border-radius:50%;background:var(--ink);display:block}
.menu{display:flex;gap:26px;font-size:11px;text-transform:uppercase;color:var(--ink);letter-spacing:.6px;align-items:center}
.menu .active{color:var(--green);border-top:2px solid var(--green);padding-top:14px;margin-top:-16px}

/* hero */
.hero{position:relative;height:380px;background:linear-gradient(90deg,#eef2f4 0%,#f7f9fa 55%,#e9eef0 100%);overflow:hidden}
.hero-copy{position:absolute;left:180px;top:100px;width:440px}
.hero-copy p{font-size:24px;font-weight:300;color:var(--ink);line-height:1.3}
.hero-copy h1{font-size:26px;font-weight:500;color:var(--ink);line-height:1.3}
.btn-dark{display:inline-block;margin-top:22px;background:var(--ink);color:#fff;font-size:10px;padding:8px 16px;border-radius:2px}
.hero-visual{position:absolute;right:150px;top:30px;width:300px;height:330px;border-radius:4px;background:linear-gradient(160deg,#e9eef0 0%,#8fcf5a 35%,#4d9a3a 55%,#c58a4a 80%,#eef2f4 100%)}

/* section headings */
.sec-title{text-align:center;font-size:26px;font-weight:400;color:var(--ink)}
.sec-lead{text-align:center;font-size:11px;line-height:1.7;color:var(--muted);margin:14px auto 0}

.welcome{padding:46px 0 40px;border-bottom:1px solid var(--line)}
.welcome .sec-lead{width:760px}

/* partners */
.partners{position:relative;height:330px}
.partners-photo{position:absolute;left:0;top:40px;width:430px;height:250px;background:linear-gradient(135deg,#d7dde2 0%,#9aa6b0 45%,#5c6b78 100%)}
.partners-copy{position:absolute;left:490px;top:50px;width:520px}
.partners-copy h2{font-size:24px;font-weight:400;color:var(--ink)}
.partners-copy > p{font-size:11px;line-height:1.7;color:var(--muted);margin-top:12px}
.features{display:grid;grid-template-columns:1fr 1fr;gap:26px 40px;margin-top:26px}
.feature{display:flex;gap:12px}
.feature svg{flex:none}
.feature h3{font-size:11px;font-weight:500;color:var(--ink);text-transform:uppercase}
.feature p{font-size:10px;line-height:1.6;color:var(--muted);margin-top:4px}

/* team */
.team{background:var(--band);height:360px;padding-top:34px}
.team .sec-title{color:#fff}
.team .sec-lead{color:#b9bec2;width:520px}
.team-grid{display:flex;justify-content:center;gap:16px;margin-top:22px}
.member{width:170px;background:#fff}
.member .photo{height:150px;background:linear-gradient(180deg,#dfe6ea 0%,#b5c2cb 100%)}
.member .name{height:30px;line-height:30px;text-align:center;font-size:12px;font-weight:500;color:var(--ink)}
.member.yellow .name{background:var(--yellow)}
.member.pink .name{background:var(--pink);color:#fff}

/* news */
.news{padding-top:36px;height:380px;position:relative;overflow:hidden}
.news .sec-lead{width:520px}
.news-row{position:absolute;top:140px;left:-90px;display:flex;gap:16px}
.card{width:262px;height:180px;border:1px solid var(--line);background:#fff;padding:16px;box-shadow:0 2px 6px rgba(0,0,0,.04)}
.card h4{font-size:12px;font-weight:500;color:var(--ink);line-height:1.45}
.card .date{font-size:9px;color:var(--muted);margin-top:6px}
.card p{font-size:10px;line-height:1.6;color:var(--muted);margin-top:8px}
.author{display:flex;align-items:center;gap:8px;margin-top:12px;font-size:9px;color:var(--muted)}
.author i{width:20px;height:20px;border-radius:50%;background:#c7ccd0;display:block}
.pager{position:absolute;top:336px;left:0;right:0;display:flex;justify-content:center;gap:6px}
.pager span{width:6px;height:6px;border-radius:50%;background:#d3d6d9}
.pager span.on{background:var(--ink)}

/* contact */
.contact{position:relative;height:660px;border-top:1px solid var(--line);overflow:hidden;background:var(--paper)}
.contact .sec-title{margin-top:44px}
.contact .sec-lead{width:420px}
.form-card{position:absolute;left:400px;top:170px;width:400px;height:420px;background:#fff;box-shadow:0 4px 20px rgba(0,0,0,.12);padding:36px 40px}
.field-label{font-size:9px;text-transform:uppercase;color:var(--ink);letter-spacing:.5px;margin-bottom:6px}
.field{height:26px;background:var(--soft);border:1px solid var(--line);margin-bottom:18px}
.row{display:flex;gap:20px}
.row > div{flex:1}
.field.area{height:80px}
.btn-submit{display:inline-block;border:1px solid var(--ink);font-size:9px;text-transform:uppercase;padding:8px 18px;color:var(--ink);margin-top:6px}

/* footer */
.footer{position:absolute;left:0;right:0;top:2370px;height:330px;background:#f7f8f9;border-top:1px solid var(--line);padding:40px 150px}
.footer-grid{display:flex;justify-content:space-between}
.footer .about{width:280px;font-size:10px;line-height:1.7;color:var(--muted)}
.footer .about p{margin-top:12px}
.footer h5{font-size:10px;text-transform:uppercase;color:var(--ink);font-weight:500;margin-bottom:14px}
.links{display:grid;grid-template-columns:110px 110px;gap:8px 20px;font-size:10px;color:var(--muted)}
.follow{display:flex;gap:10px}
.follow span{width:12px;height:12px;border-radius:50%;background:#aeb3b8;display:block}
.copyright{position:absolute;left:150px;right:150px;bottom:30px;border-top:1px solid var(--line);padding-top:14px;font-size:9px;color:var(--muted)}
</style>
</head>
<body>

<div class="topbar">
  <div class="socials"><span></span><span></span><span></span><span></span></div>
  <div class="call">
    <svg width="10" height="10" viewBox="0 0 24 24"><path d="M6.6 10.8a15 15 0 0 0 6.6 6.6l2.2-2.2a1 1 0 0 1 1-.25 11.4 11.4 0 0 0 3.6.57 1 1 0 0 1 1 1V20a1 1 0 0 1-1 1A17 17 0 0 1 3 4a1 1 0 0 1 1-1h3.5a1 1 0 0 1 1 1 11.4 11.4 0 0 0 .57 3.6 1 1 0 0 1-.25 1z" fill="#a3a8ad"/></svg>
    Call Us: +1 555 014 2280
  </div>
</div>

<nav class="nav">
  <div class="brand"><i></i>Northvale Loan</div>
  <div class="menu">
    <span class="active">Home</span><span>Overview</span><span>About Us</span><span>Team</span><span>News</span><span>Contact</span><span>Investors</span>
    <svg width="11" height="11" viewBox="0 0 24 24"><circle cx="10" cy="10" r="7" fill="none" stroke="#2f3437" stroke-width="2.5"/><path d="M15 15l6 6" stroke="#2f3437" stroke-width="2.5"/></svg>
  </div>
</nav>

<section class="hero">
  <div class="hero-copy">
    <p>We are a global structured credit investment firm.</p>
    <h1>Focused on the healthcare and technology industries</h1>
    <span class="btn-dark">Learn More</span>
  </div>
  <div class="hero-visual" role="img" aria-label="Young green plant growing from a glass jar filled with coins"></div>
</section>

<section class="welcome">
  <h2 class="sec-title">Welcome to Northvale Loan</h2>
  <p class="sec-lead">Northvale Loan provides flexible growth capital to late stage technology and healthcare companies. We structure senior and subordinated loans that help founders extend runway, fund expansion and reach key milestones without unnecessary dilution. Our team brings decades of lending, operating and investing experience to every partnership we build with management teams and investors.</p>
</section>

<section class="partners">
  <div class="partners-photo" role="img" aria-label="Business team reviewing financial charts on a laptop at a desk"></div>
  <div class="partners-copy">
    <h2>Partners for Growth</h2>
    <p>We work alongside leading venture investors to deliver tailored debt solutions for companies with proven products, strong revenue and clear paths to scale.</p>
    <div class="features">
      <div class="feature">
        <svg width="22" height="22" viewBox="0 0 24 24"><path d="M3 20h18M6 16V10M11 16V6M16 16v-8" stroke="#2f3437" stroke-width="1.6" fill="none"/></svg>
        <div><h3>Late Stage</h3><p>Capital for companies with proven models and steady revenue.</p></div>
      </div>
      <div class="feature">
        <svg width="22" height="22" viewBox="0 0 24 24"><rect x="3" y="5" width="18" height="12" rx="1" stroke="#2f3437" stroke-width="1.6" fill="none"/><path d="M8 20h8" stroke="#2f3437" stroke-width="1.6"/></svg>
        <div><h3>Technology</h3><p>Software, platforms and hardware firms ready to scale.</p></div>
      </div>
      <div class="feature">
        <svg width="22" height="22" viewBox="0 0 24 24"><path d="M12 20s-8-4.5-8-10a4.5 4.5 0 0 1 8-2.8A4.5 4.5 0 0 1 20 10c0 5.5-8 10-8 10z" stroke="#2f3437" stroke-width="1.6" fill="none"/></svg>
        <div><h3>Healthcare</h3><p>Life science and care delivery companies with growth.</p></div>
      </div>
      <div class="feature">
        <svg width="22" height="22" viewBox="0 0 24 24"><circle cx="12" cy="12" r="8" stroke="#2f3437" stroke-width="1.6" fill="none"/><path d="M8 12l3 3 5-6" stroke="#2f3437" stroke-width="1.6" fill="none"/></svg>
        <div><h3>Structured Credit</h3><p>Flexible terms designed around each business plan.</p></div>
      </div>
    </div>
  </div>
</section>

<section class="team">
  <h2 class="sec-title">Our Team</h2>
  <p class="sec-lead">Experienced lenders and operators dedicated to helping growth companies succeed.</p>
  <div class="team-grid">
    <div class="member yellow"><div class="photo" role="img" aria-label="Portrait of a team member in a suit"></div><div class="name">Daniel Archer</div></div>
    <div class="member pink"><div class="photo" role="img" aria-label="Portrait of a team member in a suit"></div><div class="name">Tomas Lindqvist</div></div>
    <div class="member yellow"><div class="photo" role="img" aria-label="Portrait of a team member in a suit"></div><div class="name">Daniel Archer</div></div>
    <div class="member pink"><div class="photo" role="img" aria-label="Portrait of a team member in a suit"></div><div class="name">Tomas Lindqvist</div></div>
  </div>
</section>

<section class="news">
  <h2 class="sec-title">Latest News</h2>
  <p class="sec-lead">Updates on recent financings, portfolio milestones and firm announcements.</p>
  <div class="news-row">
    <div class="card"><h4>Northvale closes new facility for a growing health platform</h4><div class="date">March 12, 2019</div><p>The loan will support product expansion and new hires across key markets.</p><div class="author"><i></i>Daniel Archer</div></div>
    <div class="card"><h4>Northvale closes new facility for a growing health platform</h4><div class="date">March 12, 2019</div><p>The loan will support product expansion and new hires across key markets.</p><div class="author"><i></i>Daniel Archer</div></div>
    <div class="card"><h4>Northvale closes new facility for a growing health platform</h4><div class="date">March 12, 2019</div><p>The loan will support product expansion and new hires across key markets.</p><div class="author"><i></i>Tomas Lindqvist</div></div>
    <div class="card"><h4>Northvale closes new facility for a growing health platform</h4><div class="date">March 12, 2019</div><p>The loan will support product expansion and new hires across key markets.</p><div class="author"><i></i>Daniel Archer</div></div>
    <div class="card"><h4>Northvale closes new facility for a growing health platform</h4><div class="date">March 12, 2019</div><p>The loan will support product expansion and new hires across key markets.</p><div class="author"><i></i>Tomas Lindqvist</div></div>
  </div>
  <div class="pager"><span class="on"></span><span></span><span></span></div>
</section>

<section class="contact">
  <h2 class="sec-title">Contact Us</h2>
  <p class="sec-lead">Reach out to discuss financing, investment opportunities or partnership inquiries with our team.</p>
  <div class="form-card">
    <div class="field-label">Email Address</div><div class="field"></div>
    <div class="row">
      <div><div class="field-label">First Name</div><div class="field"></div></div>
      <div><div class="field-label">Last Name</div><div class="field"></div></div>
    </div>
    <div class="field-label">Message</div><div class="field area"></div>
    <span class="btn-submit">Submit</span>
  </div>
</section>

<footer class="footer">
  <div class="footer-grid">
    <div class="about">
      <div class="brand"><i></i>Northvale Loan</div>
      <p>Northvale Loan is a structured credit investment firm providing growth capital to technology and healthcare companies.</p>
      <p>Investor Portal &nbsp;·&nbsp; info@northvaleloan.com</p>
    </div>
    <div>
      <h5>Quick Links</h5>
      <div class="links"><span>Home</span><span>Team</span><span>Overview</span><span>News</span><span>About Us</span><span>Contact</span></div>
    </div>
    <div>
      <h5>Follow Us</h5>
      <div class="follow"><span></span><span></span><span></span><span></span></div>
    </div>
  </div>
  <div class="copyright">© 2019 Northvale Loan. All rights reserved.</div>
</footer>

</body>
</html>
```